After tattoo calming solution

The label has to be modern, along the same lines as skin care brand “Plain Form.” It has to reflect the solutions natural effectiveness and simplicity. The label cannot be over fussy, and must be a little bit clinical, as it really does work. The colours should reflect that the solution calms the skin.

We use a 100ml spray bottle.

Target Market(s)

Anyone with a new tattoo or piercing

Industry/Entity Type

Skincare

Requirements
Must have
• Must reflect its natural calming but still remain a little clinical
Should not have
• It must not look like other flowery tattoo cream solutions.

```html
<!DOCTYPE html>
<html lang="en">
<head>
<meta charset="utf-8">
<title>quiet ink spray – label</title>
<link rel="stylesheet" href="https://fonts.googleapis.com/css2?family=Arimo:ital,wght@0,400;0,700;1,400&display=swap">
<style>
  :root {
    --backdrop: #cad8db;
    --label: #ffffff;
    --title: #5b777d;
    --accent-dark: #33525a;
    --volume-box: #7f9399;
    --rule: #4f6a70;
    --body-text: #1f2224;
    --caps-text: #4c6369;
  }
  * { margin: 0; padding: 0; box-sizing: border-box; }
  html, body {
    width: 1200px;
    height: 857px;
    overflow: hidden;
    background: var(--backdrop);
  }
  .canvas {
    position: relative;
    width: 1200px;
    height: 857px;
  }
  .label {
    position: absolute;
    left: 391px;
    top: 138px;
    width: 417px;
    height: 580px;
    background: var(--label);
    overflow: hidden;
  }
  .product-name {
    position: absolute;
    right: 35px;
    top: 112px;
    text-align: right;
    font-family: "Arimo", sans-serif;
    font-weight: 400;
    color: var(--title);
    line-height: 1;
  }
  .product-name .line-main {
    display: block;
    font-size: 52px;
  }
  .product-name .line-sub {
    display: block;
    font-size: 40px;
    margin-top: 4px;
  }
  .name-square {
    position: absolute;
    right: 0;
    top: 140px;
    width: 18px;
    height: 18px;
    background: var(--accent-dark);
  }
  .divider {
    position: absolute;
    left: 146px;
    top: 282px;
    width: 236px;
    height: 3px;
    background: var(--rule);
  }
  .benefits {
    position: absolute;
    right: 35px;
    top: 296px;
    width: 280px;
    text-align: right;
    font-family: "Arimo", sans-serif;
    font-style: italic;
    font-size: 19px;
    line-height: 25px;
    color: var(--body-text);
  }
  .claim {
    position: absolute;
    right: 35px;
    top: 454px;
    text-align: right;
    font-family: "Arimo", sans-serif;
    font-weight: 700;
    font-size: 14px;
    line-height: 19px;
    color: var(--caps-text);
    text-transform: uppercase;
  }
  .volume {
    position: absolute;
    left: 39px;
    top: 454px;
    width: 62px;
    height: 126px;
    background: var(--volume-box);
    color: #ffffff;
    font-family: "Arimo", sans-serif;
    font-size: 12px;
    text-align: center;
    padding-top: 21px;
  }
</style>
</head>
<body>
  <main class="canvas">
    <section class="label">
      <h1 class="product-name">
        <span class="line-main">quiet ink</span>
        <span class="line-sub">spray</span>
      </h1>
      <div class="name-square"></div>
      <div class="divider"></div>
      <p class="benefits">Reduces inflammation,<br>irritation and encourages<br>natural skin healing</p>
      <p class="claim">Expert skin repair<br>for new tattoos &amp; piercings</p>
      <div class="volume">100ml</div>
    </section>
  </main>
</body>
</html>
```